Wren Hollow Apartments
stationary
Wren Hollow Apartments - Real Estate
Creative Brief
Traditional
Tobias Lindqvist
2408 Wren Hollow Houston TX 77091
tjlindqvist@quellmail.example

```html
<!DOCTYPE html>
<html lang="en">
<head>
<meta charset="utf-8">
<title>Wren Hollow Apartments — Business Card</title>
<link rel="stylesheet" href="https://fonts.googleapis.com/css2?family=Cinzel:wght@400;600&family=Tinos:wght@400&display=swap">
<style>
  :root {
    --backdrop: #dcdcdc;
    --brand-green: #2f8f3c;
    --card-white: #ffffff;
    --ink: #3a3a3a;
    --rule-dark: #2b2b2b;
    --rule-soft: #b9b9b9;
  }
  * { margin: 0; padding: 0; box-sizing: border-box; }
  html, body {
    width: 1200px; height: 871px; overflow: hidden;
    background: var(--backdrop);
  }
  .canvas { position: relative; width: 1200px; height: 871px; }
  .card {
    position: absolute; width: 540px; height: 309px; top: 281px;
    box-shadow: 0 6px 18px rgba(0,0,0,0.18);
    overflow: hidden;
  }
  .card-front { left: 40px; background: var(--brand-green); }
  .card-back { left: 620px; background: var(--card-white); }

  .brand { position: absolute; left: 0; right: 0; text-align: center; }
  .brand-dot { display: block; margin: 0 auto; border-radius: 50%; }
  .brand-name {
    font-family: 'Cinzel', serif; font-weight: 600; letter-spacing: 1px;
    white-space: nowrap;
  }
  .card-front .brand { top: 78px; }
  .card-front .brand-dot { width: 76px; height: 76px; background: var(--card-white); }
  .card-front .brand-name { color: var(--card-white); font-size: 28px; margin-top: 16px; }

  .card-back .brand { top: 22px; }
  .card-back .brand-dot { width: 52px; height: 52px; background: var(--brand-green); }
  .card-back .brand-name { color: var(--brand-green); font-size: 22px; margin-top: 10px; }

  .holder-name {
    position: absolute; left: 40px; top: 178px;
    font-family: 'Cinzel', serif; font-weight: 600; font-size: 19px;
    color: var(--brand-green); letter-spacing: 0.5px;
  }
  .divider {
    position: absolute; left: 292px; top: 142px; width: 1px; height: 96px;
    background: var(--rule-soft);
  }
  .contact {
    position: absolute; left: 306px; top: 146px;
    font-family: 'Tinos', serif; font-size: 13.5px; color: var(--ink); line-height: 19px;
  }
  .contact-address { margin-bottom: 8px; }
  .contact-line { display: flex; align-items: center; gap: 6px; }
  .contact-line svg { width: 11px; height: 11px; flex: none; }

  .footer-rule { position: absolute; left: 0; right: 0; }
  .footer-rule.top { top: 262px; height: 2px; background: var(--rule-dark); }
  .footer-rule.band { top: 268px; height: 18px; background: var(--brand-green); }
  .footer-rule.bottom { top: 294px; height: 1px; background: var(--rule-dark); }
</style>
</head>
<body>
<div class="canvas">
  <section class="card card-front">
    <div class="brand">
      <span class="brand-dot"></span>
      <div class="brand-name">Wren Hollow Apartments</div>
    </div>
  </section>

  <section class="card card-back">
    <div class="brand">
      <span class="brand-dot"></span>
      <div class="brand-name">Wren Hollow Apartments</div>
    </div>

    <div class="holder-name">Tobias Lindqvist</div>
    <div class="divider"></div>

    <div class="contact">
      <div class="contact-address">2408 Wren Hollow<br>Houston TX 77091</div>
      <div class="contact-line">
        <svg viewBox="0 0 24 24" aria-hidden="true"><path fill="#2f8f3c" d="M6.6 10.8a15.1 15.1 0 0 0 6.6 6.6l2.2-2.2a1 1 0 0 1 1-.25 11.4 11.4 0 0 0 3.6.57 1 1 0 0 1 1 1V20a1 1 0 0 1-1 1A17 17 0 0 1 3 4a1 1 0 0 1 1-1h3.5a1 1 0 0 1 1 1c0 1.25.2 2.45.57 3.57a1 1 0 0 1-.25 1z"/></svg>
        <span>713-555-0148</span>
      </div>
      <div class="contact-line">
        <svg viewBox="0 0 24 24" aria-hidden="true"><rect x="2" y="5" width="20" height="14" fill="#2f8f3c"/><path d="M2 5l10 8 10-8" fill="none" stroke="#fff" stroke-width="2"/></svg>
        <span>tjlindqvist@quellmail.example</span>
      </div>
    </div>

    <div class="footer-rule top"></div>
    <div class="footer-rule band"></div>
    <div class="footer-rule bottom"></div>
  </section>
</div>
</body>
</html>
```